VOLT - Monitoring Natural Hazards from Space Web Application

KORMEL Sarl is a Luxembourg based Space-Startup that works in the field of Earth Observation. KORMEL is a platform able to extract value-added information from satellite data and is specialized in mapping Natural Disaster (floods, fires etc).

We are now developing a new vertical tool, called VOLT, dedicated to the monitoring of natural hazards in Humanitarian Camps around the world.

The goal of VOLT is to hide to the users' all the complexity of the Satellite Image processing and just provide them the results.

This project require to Design 4 pages of VOLT:
• Public Home Page (Code - V01)
• Dashboard (private Home Page) (Code - V03)
• Monitor (web GIS) (Code - V14)
• Registration Page (Code - V04)

We would like to provide the required time to make a good job.

Target Market(s)

Humanitarian Agencies, Goverments

Coding

Coded - Design and coding required

Number of Pages Required

4 page

Font styles to use
Other font styles liked:
• see the manual attached

Requirements
Must have
• 4 pages. One Home, one form, one dashboard and one web map.
Nice to have
• Please read the attachment with all the detailed instructions

```html
<!DOCTYPE html>
<html lang="en">
<head>
<meta charset="utf-8">
<title>VOLT – Monitoring Natural Hazards</title>
<link href="https://fonts.googleapis.com/css2?family=Jost:wght@400;500;600;700;800&display=swap" rel="stylesheet">
<style>
:root{
  --gold:#f0b83f;
  --teal:#2b4f5c;
  --teal-deep:#1f4453;
  --night:#0f2029;
  --ink:#1c2d35;
  --muted:#4a5a61;
  --line:#c9d0d3;
  --white:#ffffff;
}
*{box-sizing:border-box;margin:0;padding:0}
html,body{width:1200px;height:3499px;overflow:hidden}
body{font-family:'Jost',sans-serif;color:var(--ink);background:var(--white);position:relative}
.abs{position:absolute}
a{color:inherit;text-decoration:none}

/* header */
.site-header{position:absolute;left:0;top:0;width:1200px;height:77px;background:var(--teal)}
.brand{position:absolute;display:flex;align-items:center;gap:14px;font-weight:500;letter-spacing:4px}
.brand-dot{border:3px solid var(--gold);border-radius:50%}
.site-header .brand{left:86px;top:14px;color:var(--white);font-size:34px}
.site-header .brand-dot{width:48px;height:48px}
.main-nav{position:absolute;top:26px;left:557px;display:flex;gap:40px;color:var(--white);font-size:17px;font-weight:500}
.btn-pill{position:absolute;top:17px;height:42px;border-radius:21px;display:flex;align-items:center;justify-content:center;gap:7px;font-size:15px;font-weight:600}
.btn-register{left:863px;width:120px;background:var(--white);color:var(--teal)}
.btn-login{left:993px;width:120px;background:var(--gold);color:var(--ink)}

/* hero */
.hero{position:absolute;left:0;top:77px;width:1200px;height:639px;background:radial-gradient(ellipse at 70% 40%,#27476a 0%,#14243f 45%,#0a1426 100%)}
.hero-kicker{position:absolute;left:86px;top:132px;color:var(--white);font-size:18px;font-weight:500}
.hero-title{position:absolute;left:84px;top:160px;color:var(--white);font-size:55px;line-height:55px;font-weight:400}
.hero-title b{font-weight:700}
.hero-title .gold{color:var(--gold);font-weight:700}
.hero-text{position:absolute;left:86px;top:338px;width:440px;color:var(--white);font-size:19px;line-height:29px}
.btn-hero{position:absolute;left:86px;top:452px;width:179px;height:51px;border-radius:26px;background:var(--gold);color:var(--ink);font-size:15px;font-weight:600;display:flex;align-items:center;justify-content:center}
.hero-globe{position:absolute;left:644px;top:80px;width:468px;height:468px;border-radius:50%;border:10px solid var(--gold);background:radial-gradient(circle at 40% 35%,#4f6f80 0%,#233a4a 55%,#0f1c26 100%)}

/* partners */
.section-kicker{position:absolute;width:1200px;text-align:center;font-size:15px;font-weight:500}
.trust-title{top:776px;letter-spacing:3px;font-weight:600}
.partners{position:absolute;left:86px;top:814px;display:flex;gap:6px}
.partner{width:166px;height:82px;border:1.5px solid #9aa3a7;border-radius:4px;display:flex;align-items:center;justify-content:center;font-size:22px;font-weight:600;color:#3a3f42;letter-spacing:1px}
.partner.is-active{background:var(--gold);border-color:var(--gold);color:var(--white)}

/* description */
.desc-kicker{top:970px}
.section-title{position:absolute;width:1200px;text-align:center;font-size:41px;font-weight:400;color:var(--ink)}
.section-title b{font-weight:700}
.desc-title{top:992px}
.desc-text{position:absolute;left:210px;top:1054px;width:780px;text-align:center;font-size:17px;line-height:27px;color:var(--ink)}
.desc-earth-ring{position:absolute;left:86px;top:1192px;width:386px;height:386px;border-radius:50%;border:2px dashed var(--teal)}
.desc-earth{position:absolute;left:96px;top:1202px;width:366px;height:366px;border-radius:50%;background:radial-gradient(circle at 55% 30%,#c8dde3 0%,#5e8693 30%,#2b4f5c 65%,#16313b 100%)}
.feature{position:absolute;left:616px;display:flex;align-items:center;gap:26px}
.feature-icon{width:92px;height:92px;border-radius:50%;background:var(--gold);display:flex;align-items:center;justify-content:center}
.feature p{width:380px;font-size:20px;line-height:27px;color:var(--ink)}

/* pricing */
.pricing{position:absolute;left:0;top:1672px;width:1200px;height:747px;background:radial-gradient(ellipse at 50% 30%,#2f5868 0%,var(--teal-deep) 80%)}
.pricing .section-kicker{top:92px;color:var(--white)}
.pricing .section-title{top:112px;color:var(--white);font-weight:700}
.plan{position:absolute;top:206px;width:325px;height:443px;background:var(--white);border-radius:6px;padding:30px 29px}
.plan.is-featured{background:var(--gold)}
.plan-tag{display:inline-block;border:1.5px solid var(--gold);color:var(--gold);border-radius:14px;padding:3px 12px;font-size:12px;font-weight:600;letter-spacing:.5px}
.is-featured .plan-tag{border-color:var(--ink);color:var(--ink)}
.plan-tag.ent{border-color:#4f8a9a;color:#3d7585}
.plan-price{margin-top:14px;font-size:35px;font-weight:700;color:var(--ink);display:flex;align-items:baseline;gap:8px;height:44px}
.plan-price small{font-size:15px;font-weight:400}
.plan-sub{margin-top:8px;font-size:17px;color:var(--muted)}
.is-featured .plan-sub{color:var(--ink)}
.plan hr{border:0;border-top:1.5px solid #d7dbdd;margin:24px 0 26px}
.is-featured hr{border-top-color:#d79d2b}
.plan ul{list-style:none}
.plan li{display:flex;align-items:center;gap:9px;font-size:17px;height:34px;color:var(--ink)}
.plan-btn{position:absolute;left:29px;bottom:29px;width:267px;height:51px;border-radius:26px;background:var(--gold);display:flex;align-items:center;justify-content:center;font-size:15px;font-weight:600;color:var(--ink)}
.is-featured .plan-btn{background:var(--teal);color:var(--white)}

/* testimonials */
.stories-kicker{position:absolute;left:86px;top:2510px;font-size:15px;font-weight:500}
.stories-title{position:absolute;left:86px;top:2532px;font-size:41px;line-height:48px;font-weight:400}
.stories-title b{font-weight:700}
.slider-btn{position:absolute;top:2541px;width:55px;height:55px;border-radius:50%;border:1.5px solid #8c979b;display:flex;align-items:center;justify-content:center}
.story{position:absolute;top:2675px;width:502px;height:303px;border:1.5px dashed #4f7583;border-radius:6px;padding:0 25px}
.story-quote{position:absolute;right:-1px;top:-1px;width:86px;height:76px;background:var(--gold);border-radius:0 6px 0 76px;color:var(--ink);font-size:62px;font-weight:800;line-height:90px;text-align:right;padding-right:12px}
.stars{position:absolute;left:25px;top:32px;display:flex;gap:6px}
.story p{position:absolute;left:25px;top:86px;width:452px;font-size:17px;line-height:27px;color:var(--muted)}
.author{position:absolute;left:25px;top:212px;display:flex;align-items:center;gap:18px}
.avatar{width:64px;height:64px;border-radius:50%;background:linear-gradient(135deg,#cfd6d8,#7d8c92)}
.author strong{display:block;font-size:18px;font-weight:700;color:var(--ink)}
.author span{font-size:17px;color:var(--muted)}

/* footer */
.site-footer{position:absolute;left:0;top:3066px;width:1200px;height:433px;background:var(--night);color:var(--white)}
.site-footer .brand{left:86px;top:68px;font-size:44px;color:#2f5a68}
.site-footer .brand-dot{width:64px;height:64px}
.footer-about{position:absolute;left:86px;top:146px;width:360px;font-size:17px;line-height:30px}
.footer-col-line{position:absolute;top:0;width:1px;height:360px;background:#1f3440}
.footer-col-mark{position:absolute;top:68px;width:3px;height:24px;background:var(--gold)}
.footer-head{position:absolute;top:68px;font-size:17px;font-weight:700}
.footer-links{position:absolute;left:586px;top:100px;list-style:none;font-size:17px;line-height:34.5px}
.contact{position:absolute;left:847px;display:flex;gap:18px;font-size:17px;line-height:27px}
.contact svg{margin-top:5px;flex:none}
.footer-bottom{position:absolute;left:0;top:359px;width:1200px;border-top:1px solid #1f3440}
.copyright{position:absolute;left:86px;top:384px;font-size:15px}
.socials{position:absolute;left:881px;top:384px;display:flex;gap:20px;font-size:15px;align-items:center}
.socials span.net{font-size:12px;color:#cfd8dc}
</style>
</head>
<body>

<header class="site-header">
  <div class="brand"><span class="brand-dot"></span>VOLT</div>
  <nav class="main-nav"><a>Home</a><a>Features</a><a>Pricing</a></nav>
  <a class="btn-pill btn-register"><svg width="16" height="16" viewBox="0 0 16 16" fill="none" stroke="currentColor" stroke-width="1.5"><circle cx="7" cy="5" r="3"/><path d="M2 14c0-3 2.5-5 5-5s5 2 5 5"/></svg>Register</a>
  <a class="btn-pill btn-login"><svg width="16" height="16" viewBox="0 0 16 16" fill="none" stroke="currentColor" stroke-width="1.5"><circle cx="7" cy="5" r="3"/><path d="M2 14c0-3 2.5-5 5-5s5 2 5 5"/></svg>Login</a>
</header>

<section class="hero">
  <p class="hero-kicker">MONITORING OF NATURAL HAZARDS</p>
  <h1 class="hero-title"><b>IN HUMANITARIAN</b><br>CAMPS AROUND<br><b>THE</b> <span class="gold">WORLD.</span></h1>
  <p class="hero-text">The goal of VOLT is to hide to the users' all the complexity of the Satellite Image processing and just provide them the results.</p>
  <a class="btn-hero">View All Features</a>
  <div class="hero-globe" role="img" aria-label="Earth seen from space inside a gold ring"></div>
</section>

<p class="section-kicker trust-title">THEY TRUST IN US</p>
<div class="partners">
  <div class="partner">NORTHGATE</div>
  <div class="partner is-active">bravo</div>
  <div class="partner">Credio</div>
  <div class="partner">fivelane</div>
  <div class="partner">IOVRA</div>
  <div class="partner">KELVANO</div>
</div>

<p class="section-kicker desc-kicker">OUR DESCRIPTION</p>
<h2 class="section-title desc-title"><b>DESCRIPTION OF</b> THE TOOL</h2>
<p class="desc-text">Lorem ipsum dolor sit ameti consectetur adipisicing elit sed do eiusmod tempor incididunt ut labore et dolore magna aliqu Ut enim ad minim veniam quis nostrud exercitation ullamco labos ris nisi ut aliquip ex ea commodo consequab tuis aute iruredo lor in reprehenderit</p>

<div class="desc-earth-ring"></div>
<div class="desc-earth" role="img" aria-label="Satellite view of the Earth from orbit"></div>
<svg class="abs" style="left:460px;top:1260px" width="170" height="275" viewBox="0 0 170 275" fill="none" stroke="#5c7a84" stroke-width="3">
  <path d="M0 137 C70 137 70 4 160 4"/>
  <path d="M0 137 L160 137"/>
  <path d="M0 137 C70 137 70 270 160 270"/>
</svg>

<div class="feature" style="top:1218px">
  <div class="feature-icon"><svg width="48" height="48" viewBox="0 0 48 48" fill="none" stroke="#1c2d35" stroke-width="2"><circle cx="24" cy="24" r="18"/><ellipse cx="24" cy="24" rx="8" ry="18"/><path d="M6 24h36M9 14h30M9 34h30"/></svg></div>
  <p>Ut enim ad minim veniam quis nostrud ves exercitation ullamco labos.</p>
</div>
<div class="feature" style="top:1351px">
  <div class="feature-icon"><svg width="48" height="48" viewBox="0 0 48 48" fill="none" stroke="#1c2d35" stroke-width="2"><circle cx="28" cy="17" r="6"/><circle cx="28" cy="17" r="11" stroke-dasharray="4 3"/><path d="M4 34h8l8 4h12l10-7M12 34l8-5h8"/></svg></div>
  <p>Ut enim ad minim veniam quis nostrud ves exercitation ullamco labos.</p>
</div>
<div class="feature" style="top:1483px">
  <div class="feature-icon"><svg width="48" height="48" viewBox="0 0 48 48" fill="none" stroke="#1c2d35" stroke-width="2"><circle cx="22" cy="22" r="17"/><ellipse cx="22" cy="22" rx="7" ry="17"/><path d="M5 22h34"/><circle cx="30" cy="30" r="7" fill="#f0b83f"/><path d="M35 35l8 8"/></svg></div>
  <p>Ut enim ad minim veniam quis nostrud ves exercitation ullamco labos.</p>
</div>

<section class="pricing">
  <p class="section-kicker">OUR PRICING</p>
  <h2 class="section-title">PRICING</h2>

  <article class="plan" style="left:86px">
    <span class="plan-tag">STANDARD</span>
    <div class="plan-price">Free</div>
    <p class="plan-sub">minim veniam quis nostrud</p>
    <hr>
    <ul>
      <li><svg width="17" height="17" viewBox="0 0 16 16" fill="none" stroke="currentColor" stroke-width="1.3"><circle cx="8" cy="8" r="7"/><path d="M4.8 8.2l2.2 2.2 4.2-4.4"/></svg>Nostrud exercitation</li>
      <li><svg width="17" height="17" viewBox="0 0 16 16" fill="none" stroke="currentColor" stroke-width="1.3"><circle cx="8" cy="8" r="7"/><path d="M4.8 8.2l2.2 2.2 4.2-4.4"/></svg>Enim ad minim veniam sed</li>
      <li><svg width="17" height="17" viewBox="0 0 16 16" fill="none" stroke="currentColor" stroke-width="1.3"><circle cx="8" cy="8" r="7"/><path d="M4.8 8.2l2.2 2.2 4.2-4.4"/></svg>Commodo consequab tuis</li>
      <li><svg width="17" height="17" viewBox="0 0 16 16" fill="none" stroke="currentColor" stroke-width="1.3"><circle cx="8" cy="8" r="7"/><path d="M4.8 8.2l2.2 2.2 4.2-4.4"/></svg>Aute iruredo lor in repre</li>
    </ul>
    <a class="plan-btn">Buy Now</a>
  </article>

  <article class="plan is-featured" style="left:437px">
    <span class="plan-tag">PROFESSIONAL</span>
    <div class="plan-price">$500 <small>/per month</small></div>
    <p class="plan-sub">minim veniam quis nostrud</p>
    <hr>
    <ul>
      <li><svg width="17" height="17" viewBox="0 0 16 16" fill="none" stroke="currentColor" stroke-width="1.3"><circle cx="8" cy="8" r="7"/><path d="M4.8 8.2l2.2 2.2 4.2-4.4"/></svg>Nostrud exercitation</li>
      <li><svg width="17" height="17" viewBox="0 0 16 16" fill="none" stroke="currentColor" stroke-width="1.3"><circle cx="8" cy="8" r="7"/><path d="M4.8 8.2l2.2 2.2 4.2-4.4"/></svg>Enim ad minim veniam sed</li>
      <li><svg width="17" height="17" viewBox="0 0 16 16" fill="none" stroke="currentColor" stroke-width="1.3"><circle cx="8" cy="8" r="7"/><path d="M4.8 8.2l2.2 2.2 4.2-4.4"/></svg>Commodo consequab tuis</li>
      <li><svg width="17" height="17" viewBox="0 0 16 16" fill="none" stroke="currentColor" stroke-width="1.3"><circle cx="8" cy="8" r="7"/><path d="M4.8 8.2l2.2 2.2 4.2-4.4"/></svg>Aute iruredo lor in repre</li>
    </ul>
    <a class="plan-btn">Buy Now</a>
  </article>

  <article class="plan" style="left:788px">
    <span class="plan-tag ent">ENTERPRISE</span>
    <div class="plan-price">$699 <small>/per month</small></div>
    <p class="plan-sub">minim veniam quis nostrud</p>
    <hr>
    <ul>
      <li><svg width="17" height="17" viewBox="0 0 16 16" fill="none" stroke="currentColor" stroke-width="1.3"><circle cx="8" cy="8" r="7"/><path d="M4.8 8.2l2.2 2.2 4.2-4.4"/></svg>Nostrud exercitation</li>
      <li><svg width="17" height="17" viewBox="0 0 16 16" fill="none" stroke="currentColor" stroke-width="1.3"><circle cx="8" cy="8" r="7"/><path d="M4.8 8.2l2.2 2.2 4.2-4.4"/></svg>Enim ad minim veniam sed</li>
      <li><svg width="17" height="17" viewBox="0 0 16 16" fill="none" stroke="currentColor" stroke-width="1.3"><circle cx="8" cy="8" r="7"/><path d="M4.8 8.2l2.2 2.2 4.2-4.4"/></svg>Commodo consequab tuis</li>
      <li><svg width="17" height="17" viewBox="0 0 16 16" fill="none" stroke="currentColor" stroke-width="1.3"><circle cx="8" cy="8" r="7"/><path d="M4.8 8.2l2.2 2.2 4.2-4.4"/></svg>Aute iruredo lor in repre</li>
    </ul>
    <a class="plan-btn">Buy Now</a>
  </article>
</section>

<p class="stories-kicker">OUR DESCRIPTION</p>
<h2 class="stories-title"><b>CUSTOMER SUCCESS IS</b><br>OUR SUCCESS</h2>
<a class="slider-btn" style="left:989px"><svg width="12" height="12" viewBox="0 0 12 12" fill="none" stroke="#1c2d35" stroke-width="1.8"><path d="M8 2L4 6l4 4"/></svg></a>
<a class="slider-btn" style="left:1058px"><svg width="12" height="12" viewBox="0 0 12 12" fill="none" stroke="#1c2d35" stroke-width="1.8"><path d="M4 2l4 4-4 4"/></svg></a>

<article class="story" style="left:86px">
  <div class="story-quote">“</div>
  <div class="stars">
    <svg width="130" height="20" viewBox="0 0 130 20" fill="#1f4453"><polygon id="s1" points="10,1 12.6,7 19,7.3 14,11.4 15.7,18 10,14.3 4.3,18 6,11.4 1,7.3 7.4,7"/><use href="#s1" x="26"/><use href="#s1" x="52"/><use href="#s1" x="78"/><polygon points="114,1 116.6,7 123,7.3 118,11.4 119.7,18 114,14.3 108.3,18 110,11.4 105,7.3 111.4,7" fill="none" stroke="#1f4453" stroke-width="1.5"/></svg>
  </div>
  <p>Lorem ipsum dolor sit ameti consectetur adipisicing elit sed do eiusmod tempor incididunt ut labore et dolore magna al iqu Ut enim ad minim veniam quis nostrud exercitation ulla mco labos ris nisi ut aliquip ex ea commodo</p>
  <div class="author"><div class="avatar" role="img" aria-label="Customer portrait"></div><div><strong>MARK DEVERAN</strong><span>Customer</span></div></div>
</article>

<article class="story" style="left:611px">
  <div class="story-quote">“</div>
  <div class="stars">
    <svg width="130" height="20" viewBox="0 0 130 20" fill="#1f4453"><polygon id="s2" points="10,1 12.6,7 19,7.3 14,11.4 15.7,18 10,14.3 4.3,18 6,11.4 1,7.3 7.4,7"/><use href="#s2" x="26"/><use href="#s2" x="52"/><use href="#s2" x="78"/><polygon points="114,1 116.6,7 123,7.3 118,11.4 119.7,18 114,14.3 108.3,18 110,11.4 105,7.3 111.4,7" fill="none" stroke="#1f4453" stroke-width="1.5"/></svg>
  </div>
  <p>Lorem ipsum dolor sit ameti consectetur adipisicing elit sed do eiusmod tempor incididunt ut labore et dolore magna al iqu Ut enim ad minim veniam quis nostrud exercitation ulla mco labos ris nisi ut aliquip ex ea commodo</p>
  <div class="author"><div class="avatar" role="img" aria-label="Customer portrait"></div><div><strong>NINA SOLARO</strong><span>Customer</span></div></div>
</article>

<footer class="site-footer">
  <div class="brand"><span class="brand-dot"></span>VOLT</div>
  <p class="footer-about">The goal of VOLT is to hide to the users' all the complexity of the Satellite Image processing and just provide them the results.</p>

  <div class="footer-col-line" style="left:510px"></div>
  <div class="footer-col-line" style="left:771px"></div>
  <div class="footer-col-mark" style="left:509px"></div>
  <div class="footer-col-mark" style="left:770px"></div>

  <h3 class="footer-head" style="left:586px">QUICK LINKS</h3>
  <ul class="footer-links"><li>Home</li><li>Features</li><li>Pricing</li><li>Register</li><li>Login</li></ul>

  <h3 class="footer-head" style="left:847px">CONTACT US</h3>
  <div class="contact" style="top:100px"><svg width="14" height="16" viewBox="0 0 14 16" fill="#f0b83f"><path d="M7 0a6 6 0 0 1 6 6c0 4-6 10-6 10S1 10 1 6a6 6 0 0 1 6-6zm0 4a2 2 0 1 0 0 4 2 2 0 0 0 0-4z"/></svg><span>Ad minim veniam quis nostrud<br>dolor sit ameti consectetur</span></div>
  <div class="contact" style="top:172px"><svg width="15" height="15" viewBox="0 0 16 16" fill="#f0b83f"><path d="M3 1l3 .5 1 3.5-2 1.5a9 9 0 0 0 4.5 4.5L11 9l3.5 1 .5 3-2 2C7 15 1 9 1 3z"/></svg><span>555-018-2244</span></div>
  <div class="contact" style="top:218px"><svg width="15" height="12" viewBox="0 0 16 12" fill="#f0b83f"><path d="M0 0h16v12H0z"/><path d="M0 0l8 6 8-6" fill="none" stroke="#0f2029" stroke-width="1.4"/></svg><span>hello@voltwatch.io</span></div>

  <div class="footer-bottom"></div>
  <p class="copyright">Copyright © 2024 VOLT. All rights reserved.</p>
  <div class="socials">Social Media :<span class="net">Circlo</span><span class="net">Postr</span><span class="net">Snapgrid</span></div>
</footer>

</body>
</html>
```